Sophrologist needs a cool signage at door entrance

I need signage for dr in sophrology based in Belgium (french speaking). The signed should capture the name the "Mireille Vansteelant" - "Naturopathe-Sophrologue-Reiki" and a catchphrase = (Healthy way of life)
« Fais du bien à ton corps, pour que ton âme ait envie d’y rester »
Requirements
Must have
- Hey,
Thats the instagram account for some inspiration www.instagram.com/mireille_zen_equilibre
Light colors, green, blue
Healthy way of life
Size is 45cm wide on 30 cm high
The signage will be placed in front off woof pannel

```html
<!DOCTYPE html>
<html lang="fr">
<head>
<meta charset="utf-8">
<title>Mireille Vansteelant – Enseigne</title>
<link rel="stylesheet" href="https://fonts.googleapis.com/css2?family=Montserrat:ital,wght@1,800&family=Arimo:wght@700&display=swap">
<style>
  :root {
    --page-bg: #ffffff;
    --wood-light: #ecd9b3;
    --wood-mid: #dcc095;
    --wood-edge: #c99c62;
    --frame-dark: #5a2a12;
    --ink-green: #2e7d3c;
    --band-blue: #1e6fae;
    --band-text: #f4ecdc;
  }
  * { margin: 0; padding: 0; box-sizing: border-box; }
  html, body {
    width: 1200px;
    height: 1200px;
    overflow: hidden;
    background: var(--page-bg);
  }
  .canvas {
    position: relative;
    width: 1200px;
    height: 1200px;
  }
  .sign {
    position: absolute;
    left: 48px;
    top: 232px;
    width: 1104px;
    height: 734px;
    background:
      radial-gradient(ellipse at center, var(--wood-light) 0%, var(--wood-mid) 70%, var(--wood-edge) 100%);
  }
  .sign-frame {
    position: absolute;
    left: 18px;
    top: 18px;
    right: 18px;
    bottom: 18px;
    border: 10px solid var(--frame-dark);
    box-shadow: inset 0 0 10px rgba(60, 25, 5, 0.55), 0 0 6px rgba(60, 25, 5, 0.4);
  }
  .pill {
    position: absolute;
    left: 66px;
    width: 972px;
    border: 4px solid var(--ink-green);
    border-radius: 60px;
    display: flex;
    flex-direction: column;
    align-items: center;
    justify-content: center;
    color: var(--ink-green);
    font-family: 'Montserrat', sans-serif;
    font-style: italic;
    font-weight: 800;
    text-transform: uppercase;
    text-align: center;
  }
  .pill-name {
    top: 66px;
    height: 98px;
    font-size: 54px;
    letter-spacing: 1px;
  }
  .pill-profession {
    top: 196px;
    height: 166px;
    font-size: 42px;
    line-height: 1.15;
    letter-spacing: 1px;
  }
  .pill-catchphrase {
    top: 394px;
    height: 100px;
    font-size: 62px;
    letter-spacing: 1px;
  }
  .quote-band {
    position: absolute;
    left: 34px;
    right: 34px;
    top: 526px;
    height: 136px;
    background: var(--band-blue);
    color: var(--band-text);
    font-family: 'Arimo', sans-serif;
    font-weight: 700;
    font-size: 38px;
    line-height: 1.2;
    text-align: center;
    display: flex;
    flex-direction: column;
    justify-content: center;
  }
</style>
</head>
<body>
<div class="canvas">
  <div class="sign">
    <div class="sign-frame"></div>
    <div class="pill pill-name">Mireille Vansteelant</div>
    <div class="pill pill-profession">
      <span>Naturopathe-Sophrologue</span>
      <span>Reiki</span>
    </div>
    <div class="pill pill-catchphrase">Catchphrase</div>
    <div class="quote-band">
      <span>Fais du bien à ton corps,</span>
      <span>pour que ton âme ait envie d’y rester</span>
    </div>
  </div>
</div>
</body>
</html>
```